Creative & Appealing Business Card

Required a business card for Ferndale Recoveries
We specialise in claims management services for PPI ( Payment Protection Insurance.
2 sided business card
Round Corners
I like embossed and raised lettering

Industry/Entity Type

Business

```html
<!DOCTYPE html>
<html lang="en">
<head>
<meta charset="utf-8">
<title>Ferndale Recoveries – Business Card</title>
<link rel="stylesheet" href="https://fonts.googleapis.com/css2?family=Saira+Condensed:wght@500&family=Exo+2:wght@600&display=swap">
<style>
  :root {
    --slate: #344a54;
    --slate-soft: #5a6d76;
    --crimson: #b71f26;
    --crimson-soft: #d04a50;
    --paper: #ffffff;
    --edge: #c9c9c9;
    --shadow: #bdbdbd;
    --page: #ffffff;
  }
  * { box-sizing: border-box; margin: 0; padding: 0; }
  html, body {
    width: 1200px;
    height: 813px;
    overflow: hidden;
    background: var(--page);
  }
  .canvas {
    position: relative;
    width: 1200px;
    height: 813px;
  }
  .card {
    position: absolute;
    left: 14px;
    top: 18px;
    width: 1169px;
    height: 779px;
    border-radius: 42px;
    background: var(--paper);
    border: 1px solid var(--edge);
    box-shadow: 6px 6px 0 var(--shadow);
    overflow: hidden;
  }

  .flame-upper {
    position: absolute;
    left: 0;
    top: 0;
    width: 385px;
    height: 455px;
    border-bottom-right-radius: 60% 100%;
    background: linear-gradient(160deg, var(--crimson) 0%, var(--slate) 28%, var(--slate) 75%, var(--slate-soft) 100%);
  }
  .flame-lower {
    position: absolute;
    left: 200px;
    top: 448px;
    width: 969px;
    height: 331px;
    border-top-left-radius: 100% 60%;
    background: linear-gradient(100deg, var(--crimson-soft) 0%, var(--crimson) 35%, var(--crimson) 100%);
  }

  .brand {
    position: absolute;
    left: 394px;
    top: 194px;
    display: flex;
    align-items: center;
    gap: 20px;
  }
  .brand-mark {
    width: 150px;
    height: 150px;
    border-radius: 50%;
    background: var(--slate);
    flex: none;
  }
  .brand-name {
    font-family: "Saira Condensed", sans-serif;
    font-weight: 500;
    font-size: 76px;
    line-height: 1;
    color: var(--slate);
    white-space: nowrap;
  }
  .services {
    position: absolute;
    left: 557px;
    top: 336px;
    font-family: "Exo 2", sans-serif;
    font-weight: 600;
    font-size: 24px;
    line-height: 31px;
    color: var(--slate);
    white-space: nowrap;
  }
  .services-title {
    color: var(--crimson);
    padding-left: 12px;
  }
  .services-list { list-style: none; }
</style>
</head>
<body>
<main class="canvas">
  <section class="card">
    <div class="flame-upper" role="img" aria-label="Rising flame illustration in slate with a crimson tip"></div>
    <div class="flame-lower" role="img" aria-label="Sweeping crimson flame illustration across the lower card"></div>

    <div class="brand">
      <span class="brand-mark"></span>
      <h1 class="brand-name">Ferndale Recoveries</h1>
    </div>

    <div class="services">
      <p class="services-title">Claims Management Service for Mis-sold</p>
      <ul class="services-list">
        <li>- Payment Protection Insurance Claims</li>
        <li>- Interest Rate Hedging Products / SWAPS</li>
      </ul>
    </div>
  </section>
</main>
</body>
</html>
```